Affiliate website design and wireframe

We need a design of an affiliate website for an application we purchased, it is important that you build the website pages according to the developer of the applications specifications (please see attached documents) the developer of the application will configure the pages and add them to the site. Please take special note of his comments below.

We all so need you to create a wire frame so the developer can test everything (http://sketchwire.tolvaro.vn/)

It will be the homepage and about 16 inner pages (please see attached files)
Here is our website http://bluvendmarket.com/affiliate/affiliates/index.php

The version of the software we purchased is the Kivo Partner Hubline version

Comments from the developers

1. I will need the source files of the design (photoshop .psd files and font files if custom fonts are used), since the implementation is closely bound to component sizes (like border width, margin width etc.) and colors. If you own a corporate design manual, it's crucial to send it as well. Also, please, make sure if you use custom fonts, that these allow legal website integration (like google web fonts).

2. Any and every content is controlled via templates. All editing/adding/removing etc. is done here. The template files are essentially html/php documents, they use a template engine called quillo (http://www.quillo.net/) which has it's own language similar to php.

3. .psd files are ideal, because we deal with the specifics of KPX/KPH implementation on a daily basis. Any html/css developed in advance may prove to be a poor choice. You may choose to let an in-house developer do the job, but experience wise this is more costly, since he will not be accustomed to the template/functionality systems of KPX/KPH.

4. I will need the source files of the design (photoshop .psd files and font files if custom fonts are used), since the implementation is closely bound to component sizes (like border width, margin width etc.) and colors. If you own a corporate design manual, it's crucial to send it as well. Also, please, make sure if you use custom fonts, that these allow legal website integration (like google web fonts).

Regards,

Dorek Hanval
Multimedia Design

We prefer illustrations more than pictures of real people.

This is the home page, it is asking for Merchant and Affiliate sign up, not just affiliate.

http://bluvendmarket.com/affiliate/index.php

Please note the home page features both Merchant and Affiliate sign up

We are looking for illustration design not just stock images

Please remember the search menu that searches for the available programs, see the example we gave you, look at the search menu at the top of the page http://www.tradelumo.com/

We are reviewing everything, no need to send more designs

Target Market(s)

Natural Products Manufacturers
Natural products Sales reps
Natural Products Bloggers
Social Marketing

Industry/Entity Type

Software

Requirements
Must have
• 1. All links on pages should go to the appropriate pages.
2. Colors can be based on our logo design (look at the attachments)
3. Here is our website http://bluvendmarket.com/affiliate/affiliates/index.php
4. We have attached a drawing of how we think the homepage concept should follow.
5. Main concept of design, is trying to show our sales people (Affiliates) are doing multiple things to advertise and sell the merchants products.(see logo)
6. Need to be able to edit all text and images.
7. Our target audience is Natural product sales people (Advertisers, bloggers, ext) and natural product manufacturers.
8. You can speak to the company who made the application, through live chat, on there website http://www.kivopartnerhubline.com/
Nice to have
• See Attached Documents.
site should take up whole website pages
Look For fun Illustrated Website, one of the better ones we have seen is http://www.tradelumo.com/index.cfm
Should not have
• Please look very carefully at developers comment above.

```html
<!DOCTYPE html>
<html lang="en">
<head>
<meta charset="utf-8">
<title>Bluvend Market – Affiliate Program</title>
<link rel="stylesheet" href="https://fonts.googleapis.com/css2?family=Open+Sans:wght@400;600;700&display=swap">
<style>
  :root {
    --green: #7cc35a;
    --green-light: #8fcf6d;
    --blue: #24497a;
    --blue-dark: #1d3d68;
    --heading-blue: #2b4f86;
    --text-grey: #5a5f66;
    --white: #ffffff;
    --rule: #d9dde2;
  }
  * { box-sizing: border-box; margin: 0; padding: 0; }
  html, body {
    width: 1200px;
    height: 727px;
    overflow: hidden;
    background: var(--white);
    font-family: "Open Sans", Arial, sans-serif;
  }
  .site {
    width: 1200px;
    height: 727px;
    position: relative;
    background: var(--white);
  }

  /* Header */
  .site-header {
    height: 120px;
    position: relative;
  }
  .brand {
    position: absolute;
    left: 60px;
    top: 38px;
    display: flex;
    align-items: center;
    gap: 12px;
    font-weight: 700;
    font-size: 24px;
    color: var(--green);
    text-decoration: none;
  }
  .brand-dot {
    width: 34px;
    height: 34px;
    border-radius: 50%;
    background: var(--blue);
  }
  .account-links {
    position: absolute;
    right: 50px;
    top: 16px;
    font-size: 11px;
    color: var(--text-grey);
    text-transform: uppercase;
    letter-spacing: .3px;
  }
  .account-links a { color: inherit; text-decoration: none; }
  .account-links .divider { margin: 0 8px; }
  .main-nav {
    position: absolute;
    right: 50px;
    top: 66px;
    display: flex;
    align-items: center;
    gap: 46px;
  }
  .main-nav a {
    font-size: 12px;
    text-transform: uppercase;
    color: var(--text-grey);
    text-decoration: none;
    letter-spacing: .3px;
  }
  .main-nav a.is-active {
    border: 1px solid var(--blue);
    color: var(--blue);
    font-weight: 600;
    padding: 6px 20px;
  }

  /* Hero */
  .hero {
    display: flex;
    height: 360px;
  }
  .hero-panel {
    flex: 1;
    position: relative;
    display: flex;
    align-items: center;
    justify-content: center;
    text-align: center;
    color: var(--white);
    overflow: hidden;
  }
  .hero-panel--affiliate { background: var(--green); }
  .hero-panel--login { background: var(--blue); }
  .hero-art {
    position: absolute;
    inset: 0;
  }
  .hero-panel--affiliate .hero-art {
    background: linear-gradient(160deg, var(--green-light) 0%, var(--green) 60%, #71b851 100%);
  }
  .hero-panel--login .hero-art {
    background: linear-gradient(160deg, #2a5288 0%, var(--blue) 55%, var(--blue-dark) 100%);
  }
  .hero-content {
    position: relative;
    max-width: 420px;
  }
  .hero-title {
    font-size: 27px;
    font-weight: 700;
    text-transform: uppercase;
    letter-spacing: .5px;
    margin-bottom: 12px;
  }
  .hero-text {
    font-size: 13px;
    line-height: 1.5;
    margin-bottom: 22px;
  }
  .hero-button {
    display: inline-block;
    border: 1px solid var(--white);
    color: var(--white);
    font-size: 12px;
    text-transform: uppercase;
    text-decoration: none;
    letter-spacing: .5px;
    padding: 9px 24px;
  }

  /* How it works */
  .how-it-works {
    text-align: center;
    padding-top: 70px;
  }
  .section-title {
    font-size: 24px;
    font-weight: 600;
    text-transform: uppercase;
    color: var(--heading-blue);
    letter-spacing: .3px;
  }
</style>
</head>
<body>
<div class="site">
  <header class="site-header">
    <a class="brand" href="#">
      <span class="brand-dot"></span>
      <span class="brand-name">Bluvend Market</span>
    </a>
    <div class="account-links">
      <a href="#">Affiliate Login</a><span class="divider">|</span><a href="#">Merchant Login</a>
    </div>
    <nav class="main-nav">
      <a class="is-active" href="#">Home</a>
      <a href="#">Sign Up</a>
      <a href="#">Contact Us</a>
    </nav>
  </header>

  <section class="hero">
    <div class="hero-panel hero-panel--affiliate">
      <div class="hero-art" role="img" aria-label="Illustration of falling banknotes on green"></div>
      <div class="hero-content">
        <h2 class="hero-title">Start Making Money Now!</h2>
        <p class="hero-text">There is no charge to join our Affiliate Program.<br>Earn up to 30% commissions for all sales you referred.</p>
        <a class="hero-button" href="#">Affiliates Signup</a>
      </div>
    </div>
    <div class="hero-panel hero-panel--login">
      <div class="hero-art" role="img" aria-label="Illustration of a connected network of people icons on blue"></div>
      <div class="hero-content">
        <h2 class="hero-title">Already Our Affiliate?</h2>
        <p class="hero-text">We have always something new for our affiliates.<br>Login to check earned commissions and new campaigns.</p>
        <a class="hero-button" href="#">Login</a>
      </div>
    </div>
  </section>

  <section class="how-it-works">
    <h2 class="section-title">How Does It Work?</h2>
  </section>
</div>
</body>
</html>
```